Business card design needed

Double sided
Color, unique, elegant

Maybe put this quote somewhere?? But I think it might make it to cluttered?
“The Pilates Method of Body
Conditioning develops the body
uniformly, corrects posture, restores
vitality, invigorates the mind and
elevates the spirit”
- Lionel Hartwick

Industry/Entity Type

Business

Contact Information for Business Card

Marla Trevisick
Pilates Instructor & Personal trainer
Mobile: 0498260543
www.kovira.com.au
email: koviraheal.motion@brintmail.com

```html
<!DOCTYPE html>
<html lang="en">
<head>
<meta charset="utf-8">
<title>Kovira business card</title>
<link rel="stylesheet" href="https://fonts.googleapis.com/css2?family=Open+Sans:wght@400;600&family=Merriweather:wght@400&display=swap">
<style>
  :root {
    --paper: #ffffff;
    --ink: #1d1d1f;
    --ink-soft: #3a3a3a;
    --leaf-dark: #3b1230;
    --leaf-magenta: #b0247e;
    --leaf-violet: #7c3a8c;
    --leaf-lime: #a9d45a;
    --brand-violet: #b46fd0;
    --brand-green: #8fd36a;
  }
  * { margin: 0; padding: 0; box-sizing: border-box; }
  html, body { width: 1200px; height: 1027px; overflow: hidden; background: var(--paper); }
  .canvas { position: relative; width: 1200px; height: 1027px; font-family: "Open Sans", Arial, sans-serif; color: var(--ink); }

  .header-email {
    position: absolute; top: 4px; right: 4px;
    font-size: 16px; letter-spacing: -0.2px; color: var(--ink);
  }

  .leaf-fill {
    background:
      radial-gradient(ellipse at 30% 35%, var(--leaf-magenta) 0%, transparent 55%),
      radial-gradient(ellipse at 70% 70%, var(--leaf-violet) 0%, transparent 60%),
      linear-gradient(160deg, var(--leaf-dark) 0%, var(--leaf-magenta) 45%, var(--leaf-lime) 85%, var(--leaf-dark) 100%);
  }

  /* Front side */
  .card-front { position: absolute; left: 70px; top: 558px; width: 360px; height: 192px; }
  .strip { position: absolute; top: 0; height: 192px; border-radius: 14px; }
  .strip--1 { left: 0; width: 53px; }
  .strip--2 { left: 62px; width: 33px; }
  .strip--3 { left: 101px; width: 36px; }

  .brand { display: flex; align-items: center; gap: 5px; color: var(--brand-violet); font-weight: 600; }
  .brand-dot { width: 10px; height: 10px; border-radius: 50%; background: var(--brand-green); }
  .card-front .brand { position: absolute; right: 4px; top: 42px; font-size: 19px; letter-spacing: 1px; }

  .rule { position: absolute; left: 162px; right: 0; top: 126px; border-top: 2px dashed var(--ink); }
  .holder-name { position: absolute; right: 2px; top: 104px; font-size: 15px; font-weight: 400; }
  .details { position: absolute; right: 2px; top: 132px; text-align: right; font-size: 10.5px; line-height: 13.5px; color: var(--ink-soft); }

  /* Back side */
  .card-back { position: absolute; left: 72px; top: 789px; width: 358px; height: 210px; border-radius: 20px; }
  .back-panel { position: absolute; left: 14px; top: 16px; width: 331px; height: 180px; background: var(--paper); border-radius: 18px; }
  .quote {
    position: absolute; left: 13px; top: 64px; width: 230px;
    font-family: "Merriweather", Georgia, serif; font-size: 10px; line-height: 13.5px; color: var(--ink);
  }
  .card-back .brand { position: absolute; right: 16px; top: 60px; font-size: 19px; letter-spacing: 1px; }
</style>
</head>
<body>
<div class="canvas">
  <p class="header-email">koviraheal.motion@brintmail.com</p>

  <section class="card-front">
    <div class="strip strip--1 leaf-fill" role="img" aria-label="Close-up photo of purple and magenta leaves with lime edges"></div>
    <div class="strip strip--2 leaf-fill" role="img" aria-label="Close-up photo of purple and magenta leaves with lime edges"></div>
    <div class="strip strip--3 leaf-fill" role="img" aria-label="Close-up photo of purple and magenta leaves with lime edges"></div>

    <div class="brand"><span class="brand-dot"></span>Kovira</div>

    <p class="holder-name">Marla Trevisick</p>
    <div class="rule"></div>
    <div class="details">
      <p>Pilates Instructor &amp; Personal trainer</p>
      <p>koviraheal.motion@brintmail.com</p>
      <p>www.kovira.com.au</p>
      <p>Mobile: 0498260543</p>
    </div>
  </section>

  <section class="card-back leaf-fill" role="img" aria-label="Border of purple and magenta leaf photography">
    <div class="back-panel">
      <p class="quote">"The Pilates Method of Body Conditioning<br>develops the body uniformly, corrects<br>posture, restores vitality, invigorates<br>the mind and elevates the spirit"<br>- Lionel Hartwick</p>
      <div class="brand"><span class="brand-dot"></span>Kovira</div>
    </div>
  </section>
</div>
</body>
</html>
```